Branding Banner For Viral Food Truck

Our food truck has gone viral on Flickstream and we're now requesting a banner to be displayed

Size: 6x2.5 landscape

Tacos
Shucos
Churrasco
Aguas Fresca Y Más

LOGO - Pereira's Torta Spot
W Hollister Ave (Entrada/Entrance Brindle Shopping Center)
Larkmere, NY 11990

Para horarios y información / For pop-up, updated hours and information
Síganos/Follow Us (Chatterbook, Snapgallery & Flickstream logos): @pereirastortaspot

```html
<!DOCTYPE html>
<html lang="es">
<head>
<meta charset="utf-8">
<title>Pereira's Torta Spot Banner</title>
<link href="https://fonts.googleapis.com/css2?family=Squada+One&family=Montserrat:wght@500;600;700&display=swap" rel="stylesheet">
<style>
  :root {
    --stage-grey: #8c8c8c;
    --banner-red: #e4232b;
    --banner-red-deep: #c41a22;
    --rule-dark: #5a0e10;
    --cream: #f7e2b8;
    --ink: #1d1d1d;
    --white: #ffffff;
  }
  * { margin: 0; padding: 0; box-sizing: border-box; }
  html, body { width: 1200px; height: 572px; overflow: hidden; }
  body {
    background: var(--stage-grey);
    font-family: "Montserrat", sans-serif;
    position: relative;
  }
  .banner {
    position: absolute; left: 62px; top: 56px;
    width: 1076px; height: 431px;
    box-shadow: 3px 5px 8px rgba(0,0,0,.35);
    background: var(--white);
  }
  .banner__field {
    position: absolute; left: 0; top: 0; width: 100%; height: 371px;
    background: radial-gradient(ellipse at 55% 100%, var(--banner-red) 0%, var(--banner-red) 45%, var(--banner-red-deep) 100%);
    overflow: hidden;
  }
  .banner__frame {
    position: absolute; left: 21px; top: 22px; width: 1034px; height: 331px;
    border: 1px solid var(--rule-dark);
  }
  .star-row {
    position: absolute; width: 108px; height: 20px;
    background: var(--rule-dark); opacity: .55; border-radius: 10px;
  }
  .star-row--left { left: 128px; top: 62px; }
  .star-row--right { left: 472px; top: 62px; }
  .headline {
    position: absolute; left: 0; top: 36px; width: 710px;
    text-align: center; color: var(--white);
    font-family: "Squada One", sans-serif; font-weight: 400;
    font-size: 72px; line-height: 67px; letter-spacing: 1px;
  }
  .divider {
    position: absolute; left: 77px; top: 261px; width: 552px; height: 1px;
    background: var(--rule-dark);
  }
  .divider__flourish {
    position: absolute; left: 50%; top: -8px; width: 130px; height: 16px;
    transform: translateX(-50%); background: var(--banner-red);
  }
  .divider__flourish::after {
    content: ""; position: absolute; left: 10px; right: 10px; top: 4px; bottom: 4px;
    border-radius: 8px; background: var(--rule-dark); opacity: .6;
  }
  .address {
    position: absolute; left: 0; top: 280px; width: 710px;
    text-align: center; color: var(--white);
  }
  .address__street { font-size: 25px; font-weight: 700; line-height: 32px; }
  .address__note { font-size: 18px; font-weight: 500; line-height: 24px; }
  .brand-mark {
    position: absolute; left: 697px; top: 40px; width: 294px; height: 294px;
    border-radius: 50%; background: var(--cream);
    display: flex; align-items: center; justify-content: center;
    text-align: center;
  }
  .brand-mark__name {
    font-family: "Squada One", sans-serif; font-size: 44px; line-height: 46px;
    color: var(--ink); width: 230px;
  }
  .info-bar {
    position: absolute; left: 0; top: 371px; width: 100%; height: 60px;
    display: flex; align-items: center; justify-content: space-between;
    padding: 0 24px 0 38px; color: var(--ink); white-space: nowrap;
  }
  .info-bar__hours { font-size: 12.5px; font-weight: 500; }
  .follow { display: flex; align-items: center; gap: 9px; }
  .follow__label { font-size: 13px; font-weight: 500; }
  .follow__networks { display: flex; gap: 5px; }
  .follow__network { font-size: 8.5px; font-weight: 700; color: var(--banner-red); }
  .follow__handle { font-size: 15px; font-weight: 700; }
  .caption {
    position: absolute; left: 0; top: 514px; width: 100%;
    text-align: center; font-size: 17px; color: var(--ink);
  }
</style>
</head>
<body>
  <section class="banner">
    <div class="banner__field">
      <div class="banner__frame"></div>
      <div class="star-row star-row--left" role="img" aria-label="Row of decorative stars"></div>
      <div class="star-row star-row--right" role="img" aria-label="Row of decorative stars"></div>
      <h1 class="headline">TACOS,<br>SHUCOS, CHURRASCO<br>AGUAS FRESCA Y MÁS</h1>
      <div class="divider"><span class="divider__flourish" role="img" aria-label="Decorative scroll flourish"></span></div>
      <div class="address">
        <p class="address__street">W Hollister Ave Larkmere, NY 11990</p>
        <p class="address__note">(Entrada/Entrance Brindle Shopping Center)</p>
      </div>
      <div class="brand-mark">
        <span class="brand-mark__name">Pereira's Torta Spot</span>
      </div>
    </div>
    <footer class="info-bar">
      <p class="info-bar__hours">Para horarios y información / For pop-up, updated hours and information</p>
      <div class="follow">
        <span class="follow__label">Síganos/Follow US</span>
        <span class="follow__networks">
          <span class="follow__network">Chatterbook</span>
          <span class="follow__network">Snapgallery</span>
          <span class="follow__network">Flickstream</span>
        </span>
        <span class="follow__handle">@pereirastortaspot</span>
      </div>
    </footer>
  </section>
  <p class="caption">Design Concept 01</p>
</body>
</html>
```